Recipe mobile app, new flow and design for uploading recipe process

I need a new recipe upload process that's simple, intuitive, and engaging.
The goal is to have a user-friendly and fast flow.
The app is a social recipe library where anyone can upload a recipe after signing up. I currently have a flow, but it's "boring," so I'd like to significantly improve this aspect of the app.
When I create a new recipe, it's immediately saved and labeled as a draft. I'll then need to specify:
- Recipe title
- Cover image (required)
- Number of people (how many people is the recipe for)
- Ingredients (name, quantity, and unit of measurement)
- Recipe explanation (broken down into steps, and I can optionally attach an image to each step)
- Upload
Every change is immediately saved, so you can edit, exit, and resume editing later.
I've attached images of the app and the current upload process.
Thank you.
Low design quality
Good morning everyone,
some of the designs received are fantastic, but please make sure to carefully read the requirement so as not to do extra work.
The requirement is to redesign the flow that a user follows when uploading a recipe to the platform.
We have uploaded the current app screens to give you an idea of what the product looks like, what the colors and style are, but we don’t need a full redesign - only the part mentioned above, while keeping the existing style and colors (we cannot rework the entire theme).
To clarify: if you look at the screens shared in the zip file attached to the project, the focus should be on the screens from 5_.png to 10_.png.
These screens can be redesigned in the most creative way you think, as long as the overall theme remains unchanged.
Thank you for your attention.

```html
<!DOCTYPE html>
<html lang="en">
<head>
<meta charset="utf-8">
<title>Recipe Upload Flow</title>
<link href="https://fonts.googleapis.com/css2?family=Poppins:wght@300;400;500;600&display=swap" rel="stylesheet">
<style>
  :root {
    --backdrop: #24a35b;
    --brand: #1f9d55;
    --surface: #ffffff;
    --screen: #f1f1f1;
    --field: #f4f4f4;
    --ink: #222222;
    --ink-soft: #3a3a3a;
    --muted: #a2a2a2;
    --line: #e6e6e6;
  }
  * { box-sizing: border-box; margin: 0; padding: 0; }
  html, body { width: 1200px; height: 595px; overflow: hidden; background: var(--backdrop); }
  body { font-family: "Poppins", sans-serif; color: var(--ink); }
  .stage { position: absolute; left: 0; top: 0; width: 2576px; height: 1278px; transform: scale(0.46584); transform-origin: 0 0; }
  .phone { position: absolute; top: 117px; width: 443px; height: 961px; background: var(--screen); border-radius: 40px; overflow: hidden; }
  .phone.tall { height: 1061px; }
  .abs { position: absolute; }
  .status { position: absolute; left: 0; top: 0; width: 100%; height: 105px; background: var(--surface); }
  .status .time { position: absolute; left: 37px; top: 14px; font-size: 18px; font-weight: 500; }
  .status .icons { position: absolute; right: 17px; top: 19px; }
  .status .back { position: absolute; left: 35px; top: 70px; }
  .status h1 { position: absolute; left: 0; right: 0; top: 58px; text-align: center; font-size: 25px; font-weight: 500; color: var(--ink-soft); }
  .card { position: absolute; background: var(--surface); border-radius: 10px; }
  .dashed { position: absolute; border: 3px dashed var(--brand); border-radius: 6px; display: flex; flex-direction: column; align-items: center; justify-content: center; text-align: center; }
  .hint { font-size: 14.5px; font-weight: 300; color: var(--muted); line-height: 1.45; }
  .field { position: absolute; background: var(--surface); border-radius: 8px; font-size: 17px; display: flex; align-items: center; padding-left: 14px; }
  .field.placeholder { color: var(--muted); font-weight: 300; }
  .btn { position: absolute; background: var(--brand); color: #fff; border-radius: 22px; font-size: 19px; font-weight: 500; display: flex; align-items: center; justify-content: center; box-shadow: 0 3px 6px rgba(0,0,0,.12); }
  .btn.small { border-radius: 20px; font-size: 19px; gap: 6px; }
  .home-bar { position: absolute; left: 143px; width: 158px; height: 5px; border-radius: 3px; background: #c8c8c8; }
  .section-title { position: absolute; left: 29px; top: 376px; font-size: 16.5px; font-weight: 500; color: var(--ink-soft); }
  .draft-label { position: absolute; left: 8px; top: 190px; font-size: 14.5px; font-weight: 500; }
  .draft-edit { position: absolute; right: 10px; top: 196px; }
  .photo { position: absolute; border-radius: 8px; }
  .nav { position: absolute; left: 0; top: 848px; width: 100%; height: 113px; background: var(--surface); }
  .nav-item { position: absolute; top: 20px; width: 80px; text-align: center; font-size: 11.5px; color: var(--muted); }
  .nav-item svg { display: block; margin: 0 auto 10px; }
  .nav-item.active { color: var(--brand); font-weight: 500; }
  .nav-add { position: absolute; left: 197px; top: -3px; width: 50px; height: 50px; border-radius: 50%; background: var(--surface); }
  .serves { position: absolute; background: var(--surface); border-radius: 8px; font-size: 14px; font-weight: 500; display: flex; align-items: center; }
  .ingredient { position: absolute; left: 30px; width: 383px; height: 98px; }
  .ingredient .name { position: absolute; left: 14px; top: 9px; font-size: 19px; font-weight: 600; }
  .ingredient .name.placeholder { color: #8a8a8a; font-weight: 500; }
  .qty { position: absolute; left: 14px; top: 45px; width: 180px; height: 44px; border: 1.5px solid var(--line); border-radius: 8px; font-size: 18px; font-weight: 500; display: flex; align-items: center; justify-content: center; }
  .unit { position: absolute; left: 211px; top: 45px; width: 163px; height: 44px; background: var(--field); border-radius: 8px; font-size: 16.5px; display: flex; align-items: center; padding-left: 38px; }
  .unit svg { position: absolute; right: 14px; top: 17px; }
  .muted-text { color: #8a8a8a; }
  .step { position: absolute; left: 30px; width: 383px; height: 170px; }
  .step-tab { position: absolute; left: 0; top: 0; width: 40px; height: 40px; background: var(--brand); border-radius: 10px 0 40px 0; color: #fff; font-size: 16px; font-weight: 500; padding: 4px 0 0 10px; }
  .step-text { position: absolute; left: 15px; top: 45px; width: 226px; height: 111px; border: 1.5px solid var(--line); border-radius: 8px; padding: 8px 8px; font-size: 15.5px; line-height: 1.55; color: #444; overflow: hidden; }
  .step-text.placeholder { color: var(--muted); }
  .step-photo { position: absolute; left: 260px; top: 45px; width: 113px; height: 112px; border-radius: 8px; }
</style>
</head>
<body>
<svg width="0" height="0" style="position:absolute">
  <defs>
    <symbol id="status-icons" viewBox="0 0 78 14">
      <rect x="0" y="9" width="3" height="4" rx="1" fill="#222"/><rect x="5" y="7" width="3" height="6" rx="1" fill="#222"/><rect x="10" y="4" width="3" height="9" rx="1" fill="#222"/><rect x="15" y="1" width="3" height="12" rx="1" fill="#bbb"/>
      <path d="M28 5a11 11 0 0 1 15 0l-2 2a8 8 0 0 0-11 0z M31 8a6 6 0 0 1 9 0l-2 2a3 3 0 0 0-5 0z M35.5 13l-2-2a3 3 0 0 1 4 0z" fill="#222"/>
      <rect x="50" y="1" width="24" height="12" rx="3" fill="none" stroke="#999" stroke-width="1"/><rect x="52" y="3" width="20" height="8" rx="1.5" fill="#222"/><rect x="75" y="5" width="2" height="4" rx="1" fill="#999"/>
    </symbol>
    <symbol id="back" viewBox="0 0 14 16"><path d="M13 1v14L1 8z" fill="#1f9d55"/></symbol>
    <symbol id="camera" viewBox="0 0 40 34"><path d="M13 2h14l3 5h6a4 4 0 0 1 4 4v19a4 4 0 0 1-4 4H4a4 4 0 0 1-4-4V11a4 4 0 0 1 4-4h6z" fill="#1f9d55"/><circle cx="20" cy="19" r="7.5" fill="#fff"/><circle cx="20" cy="19" r="4.5" fill="#1f9d55"/></symbol>
    <symbol id="chevron" viewBox="0 0 14 9"><path d="M1 1l6 6 6-6" fill="none" stroke="#333" stroke-width="2"/></symbol>
    <symbol id="pencil" viewBox="0 0 12 12"><path d="M1 11l1-3 6-6 2 2-6 6z" fill="#aaa"/></symbol>
    <symbol id="plus-circle" viewBox="0 0 40 40"><circle cx="20" cy="20" r="18" fill="none" stroke="#1f9d55" stroke-width="3"/><path d="M20 10v20M10 20h20" stroke="#1f9d55" stroke-width="3"/></symbol>
    <symbol id="plus" viewBox="0 0 16 16"><path d="M8 1v14M1 8h14" stroke="#fff" stroke-width="2.4"/></symbol>
  </defs>
</svg>

<div class="stage">

  <!-- Screen 1: New recipe / drafts -->
  <section class="phone" style="left:57px">
    <header class="status">
      <span class="time">9:41</span>
      <svg class="icons" width="78" height="14"><use href="#status-icons"/></svg>
      <svg class="back" width="14" height="16"><use href="#back"/></svg>
      <h1>New Recipe</h1>
    </header>
    <div class="card" style="left:29px;top:133px;width:384px;height:225px">
      <div class="dashed" style="left:9px;top:9px;right:9px;bottom:9px">
        <svg width="40" height="40" style="margin-top:-10px"><use href="#plus-circle"/></svg>
        <p class="hint" style="margin-top:25px">Tap here to add a new recipe in drafts.</p>
      </div>
    </div>
    <h2 class="section-title">Your Recipe Drafts</h2>
    <div class="card" style="left:27px;top:420px;width:189px;height:223px">
      <div class="dashed" style="left:8px;top:8px;width:173px;height:173px">
        <svg width="24" height="20"><use href="#camera"/></svg>
        <p class="hint" style="margin-top:8px">Tap here to to upload<br>a cover picture.</p>
      </div>
      <span class="draft-label">Recipe Name</span>
      <svg class="draft-edit" width="12" height="12"><use href="#pencil"/></svg>
    </div>
    <div class="card" style="left:227px;top:420px;width:191px;height:223px">
      <div class="photo" role="img" aria-label="Plate of penne in white sauce" style="left:8px;top:8px;width:174px;height:173px;background:linear-gradient(135deg,#e9d9a8,#c9a964 55%,#8e7440)"></div>
      <span class="draft-label">White Sauce Pasta</span>
      <svg class="draft-edit" width="12" height="12"><use href="#pencil"/></svg>
    </div>
    <div class="card" style="left:27px;top:653px;width:189px;height:223px">
      <div class="dashed" style="left:8px;top:8px;width:173px;height:173px">
        <svg width="24" height="20"><use href="#camera"/></svg>
        <p class="hint" style="margin-top:8px">Tap here to to upload<br>a cover picture.</p>
      </div>
    </div>
    <nav class="nav">
      <div class="nav-item" style="left:6px"><svg width="22" height="22" viewBox="0 0 22 22"><path d="M11 2l9 8v10h-6v-6H8v6H2V10z" fill="#b5b5b5"/></svg>HOME</div>
      <div class="nav-item" style="left:87px"><svg width="22" height="22" viewBox="0 0 22 22"><path d="M4 1h14v20l-7-5-7 5z" fill="#b5b5b5"/></svg>FAVORITE</div>
      <div class="nav-add"><svg width="50" height="50" viewBox="0 0 40 40"><use href="#plus-circle"/></svg></div>
      <div class="nav-item active" style="left:182px;top:62px">NEW RECIPE</div>
      <div class="nav-item" style="left:277px"><svg width="22" height="22" viewBox="0 0 22 22"><circle cx="11" cy="6" r="5" fill="#b5b5b5"/><path d="M2 21c0-6 4-9 9-9s9 3 9 9z" fill="#b5b5b5"/></svg>ACCOUNT</div>
      <div class="nav-item" style="left:359px"><svg width="22" height="22" viewBox="0 0 22 22"><path d="M1 4h20M1 11h20M1 18h20" stroke="#b5b5b5" stroke-width="2.4"/></svg>MENU</div>
      <div class="home-bar" style="top:103px"></div>
    </nav>
  </section>

  <!-- Screen 2: Add recipe, empty -->
  <section class="phone" style="left:557px">
    <header class="status">
      <span class="time">9:41</span>
      <svg class="icons" width="78" height="14"><use href="#status-icons"/></svg>
      <svg class="back" width="14" height="16"><use href="#back"/></svg>
      <h1>Add Recipe</h1>
    </header>
    <div class="field placeholder" style="left:29px;top:133px;width:383px;height:45px">Type Recipe Name here</div>
    <div class="card" style="left:29px;top:205px;width:383px;height:383px">
      <div class="dashed" style="left:19px;top:19px;width:346px;height:346px">
        <svg width="40" height="34" style="margin-top:-30px"><use href="#camera"/></svg>
        <p class="hint" style="margin-top:58px">Tap here to capture a photo<br>or upload a photo from storage.</p>
      </div>
    </div>
    <div class="btn" style="left:43px;top:648px;width:360px;height:43px">Next</div>
    <div class="home-bar" style="top:948px"></div>
  </section>

  <!-- Screen 3: Add recipe, filled -->
  <section class="phone" style="left:1057px">
    <header class="status">
      <span class="time">9:41</span>
      <svg class="icons" width="78" height="14"><use href="#status-icons"/></svg>
      <svg class="back" width="14" height="16"><use href="#back"/></svg>
      <h1>Add Recipe</h1>
    </header>
    <div class="field" style="left:29px;top:133px;width:383px;height:45px;font-weight:500;color:var(--ink-soft)">Birthday Cake</div>
    <div class="photo" role="img" aria-label="Mint frosted birthday cake with cherries on a plate" style="left:29px;top:205px;width:383px;height:383px;background:radial-gradient(ellipse at 50% 45%,#cfe6dc 0 22%,#d9c7cf 30%,#9a8d88 48%,#6b4a35 72%,#4a3020)"></div>
    <div class="btn" style="left:43px;top:648px;width:360px;height:43px">Next</div>
    <div class="home-bar" style="top:948px"></div>
  </section>

  <!-- Screen 4: Ingredients -->
  <section class="phone" style="left:1557px">
    <header class="status">
      <span class="time">9:41</span>
      <svg class="icons" width="78" height="14"><use href="#status-icons"/></svg>
      <svg class="back" width="14" height="16"><use href="#back"/></svg>
      <h1>Ingredients</h1>
    </header>
    <div class="serves" style="left:30px;top:133px;width:275px;height:44px;padding-left:8px">For how many persons is this recipe ?</div>
    <div class="serves" style="left:321px;top:133px;width:92px;height:44px;padding-left:12px;font-size:19px;font-weight:600;gap:8px">
      <svg width="18" height="18" viewBox="0 0 22 22"><circle cx="11" cy="6" r="5" fill="#1f9d55"/><path d="M2 21c0-6 4-9 9-9s9 3 9 9z" fill="#1f9d55"/></svg>04
      <svg width="12" height="8"><use href="#chevron"/></svg>
    </div>

    <div class="card ingredient" style="top:205px"><span class="name">Milk</span><div class="qty">100</div><div class="unit">Milliliters<svg width="14" height="9"><use href="#chevron"/></svg></div></div>
    <div class="card ingredient" style="top:323px"><span class="name">Sugar</span><div class="qty">1</div><div class="unit">as needed<svg width="14" height="9"><use href="#chevron"/></svg></div></div>
    <div class="card ingredient" style="top:440px"><span class="name">Chocolate</span><div class="qty">10</div><div class="unit" style="padding-left:45px">Grams<svg width="14" height="9"><use href="#chevron"/></svg></div></div>
    <div class="card ingredient" style="top:558px"><span class="name">Eggs</span><div class="qty">5</div><div class="unit" style="padding-left:47px">Pieces<svg width="14" height="9"><use href="#chevron"/></svg></div></div>
    <div class="card ingredient" style="top:675px"><span class="name placeholder">Ingredient name</span><div class="qty muted-text">0</div><div class="unit muted-text" style="padding-left:56px">Unit<svg width="14" height="9"><use href="#chevron"/></svg></div></div>

    <div class="btn small" style="left:325px;top:793px;width:88px;height:42px">Add<svg width="16" height="16"><use href="#plus"/></svg></div>
    <div class="btn" style="left:43px;top:856px;width:358px;height:44px">Next</div>
    <div class="home-bar" style="top:948px"></div>
  </section>

  <!-- Screen 5: Steps -->
  <section class="phone tall" style="left:2057px">
    <header class="status">
      <span class="time">9:41</span>
      <svg class="icons" width="78" height="14"><use href="#status-icons"/></svg>
      <svg class="back" width="14" height="16"><use href="#back"/></svg>
      <h1>Steps</h1>
    </header>

    <div class="card step" style="top:133px">
      <span class="step-tab">1</span>
      <p class="step-text">In a bowl whisk flour, sugar, baking powder, and salt until evenly combined.</p>
      <div class="step-photo" role="img" aria-label="Glass bowl with flour and a cracked egg" style="background:radial-gradient(circle at 55% 45%,#f0b43a 0 10%,#e8e4dc 22%,#b9b5ad 60%,#8c8780)"></div>
    </div>
    <div class="card step" style="top:323px">
      <span class="step-tab">2</span>
      <p class="step-text">In a separate bowl, beat the softened butter until smooth. Add the eggs one at a time, beating briefly…</p>
      <div class="step-photo" role="img" aria-label="Bowl of creamed butter and eggs" style="background:radial-gradient(circle at 50% 50%,#f2ecb6 0 40%,#d8d2a0 55%,#a9a69a 80%)"></div>
    </div>
    <div class="card step" style="top:513px">
      <span class="step-tab">3</span>
      <p class="step-text">Scrape batter into the prepared pan and smooth the top with an offset spatula or the back of a s…</p>
      <div class="step-photo" role="img" aria-label="Pan of smoothed cake batter with a spoon" style="background:radial-gradient(circle at 45% 55%,#f5eeb0 0 38%,#e2d69a 50%,#b98a6a 75%,#9c6f52)"></div>
    </div>
    <div class="card step" style="top:703px">
      <span class="step-tab">4</span>
      <p class="step-text placeholder">Type step description here.</p>
      <div class="dashed" style="left:270px;top:53px;width:93px;height:94px;border-width:2px">
        <svg width="24" height="20"><use href="#camera"/></svg>
      </div>
    </div>

    <div class="btn small" style="left:324px;top:892px;width:89px;height:42px">Add<svg width="16" height="16"><use href="#plus"/></svg></div>
    <div class="btn" style="left:44px;top:955px;width:360px;height:44px">Upload Recipe</div>
  </section>

</div>
</body>
</html>
```